Medigap Insurance Interactive website

We are looking at redesigning our website for a more up to date and responsive look and feel. We will code this site using Bootstrap 3 so please research and know how to design for this. Attached is our logo and a wireframe for the new site.
I look forward to seeing what you guys can do.

Target Market(s)

People elegible for Medigap Insurance in the US

Industry/Entity Type

Insurance

Number of Pages Required

5+ page

Font styles to use
Sans Serif

Requirements
Must have
• Match the logo
• Be Bootstrap 3 compatible design
• Font Awesome Icons

```html
<!DOCTYPE html>
<html lang="en">
<head>
<meta charset="utf-8">
<title>Careplan360</title>
<link rel="stylesheet" href="https://fonts.googleapis.com/css2?family=Signika:wght@300;400;600&family=Dancing+Script:wght@400&display=swap">
<style>
:root{
  --navy:#0d2f63;
  --navy-deep:#0a2450;
  --red:#b3241c;
  --red-text:#c0281e;
  --ink:#222;
  --body:#444;
  --line:#d5d5d5;
  --footer:#dedede;
  --white:#fff;
}
*{margin:0;padding:0;box-sizing:border-box}
html,body{width:1200px;height:908px;overflow:hidden;background:var(--white)}
body{position:relative;font-family:'Signika',sans-serif;color:var(--body)}
.abs{position:absolute}

.site-header{left:0;top:0;width:1200px;height:65px;background:var(--white)}
.brand{left:37px;top:20px;font-size:22px;font-weight:400;color:var(--navy);letter-spacing:.5px;line-height:24px}
.brand-bar{left:37px;top:45px;width:135px;height:3px;background:var(--navy)}
.main-nav{left:0;top:0;height:65px}
.main-nav a{position:absolute;top:26px;font-size:14px;color:#222;text-decoration:none;white-space:nowrap}
.main-nav .active::after{content:"";position:absolute;left:-2px;right:0;top:33px;height:3px;background:var(--red)}
.header-divider{top:0;width:1px;height:65px;background:var(--line)}
.contact{left:898px;top:13px;width:204px;text-align:center}
.contact .cta{font-size:15px;color:var(--red-text);letter-spacing:.3px}
.contact .phone{font-size:17px;color:#333;letter-spacing:.5px;margin-top:2px}
.social{left:1118px;top:14px;width:48px}
.social span{float:left;width:19px;height:19px;margin:0 4px 4px 0;background:#111;border-radius:3px}

.hero{left:0;top:65px;width:1200px;height:443px;background:linear-gradient(135deg,#1b3e72,#0f2c5c 60%,#143766)}
.why-card{left:36px;top:136px;width:666px;height:308px;background:linear-gradient(90deg,#fbfbfb 0%,#eeeae6 40%,#7a6a5e 62%,#3a3432 80%,#c9bdb1 100%)}
.why-card h2{position:absolute;left:21px;top:36px;font-size:31px;font-weight:600;color:#222}
.why-card p{position:absolute;left:23px;top:86px;width:260px;font-size:14px;line-height:23px;font-weight:300;color:#333}
.why-card .more{position:absolute;left:23px;top:160px;font-size:14px;color:var(--red-text);text-decoration:none}
.video{left:740px;top:136px;width:426px;height:308px;background:var(--white);padding:3px}
.video-frame{position:relative;width:420px;height:302px;overflow:hidden;background:linear-gradient(180deg,#c9d3d6,#9aa7aa 55%,#6b6a70)}
.ribbon{position:absolute;right:-32px;top:22px;width:150px;height:28px;background:var(--red);transform:rotate(45deg);color:#fff;font-size:12px;text-align:center;line-height:28px;letter-spacing:.5px}
.play{position:absolute;left:175px;top:110px;width:64px;height:64px;border-radius:50%;background:#151515}
.controls{position:absolute;left:0;bottom:0;width:420px;height:34px;background:#1b1b1b}

.action-band{left:0;top:508px;width:1200px;height:85px;background:var(--red)}
.action-band a{position:absolute;top:26px;font-size:25px;font-weight:600;color:#fff;text-decoration:none;transform:translateX(-50%);white-space:nowrap}
.action-band .focus{left:581px;top:21px;width:222px;height:44px;border:1px solid rgba(255,255,255,.8)}

.card{top:632px;height:196px;border:1px solid var(--line);background:#fff}
.quote-card{left:37px;width:325px}
.quote-card p{position:absolute;left:15px;top:20px;width:300px;font-family:'Dancing Script',cursive;font-size:15px;line-height:25px;color:#222}
.reviews{left:381px;width:371px}
.card h3{position:absolute;left:19px;top:16px;font-size:30px;font-weight:400;color:#222}
.reviews p{position:absolute;left:19px;top:74px;width:340px;font-size:13.5px;line-height:23px;font-weight:300;color:#333}
.reviews .by{position:absolute;left:21px;top:147px;font-size:13.5px;color:var(--navy)}
.updates{left:772px;width:384px}
.signup{position:absolute;left:21px;top:72px;width:336px;height:40px;display:flex}
.signup .email{flex:1;background:#ececec;border:1px solid #ccc;font-size:14px;color:#666;padding:11px 10px}
.signup .btn{width:105px;background:var(--navy-deep);color:#fff;font-size:18px;font-weight:600;text-align:center;line-height:40px}
.updates .note{position:absolute;left:21px;top:153px;font-size:12.5px;color:var(--navy)}

.site-footer{left:0;top:864px;width:1200px;height:44px;background:var(--footer);text-align:center;font-size:14px;color:#444;line-height:44px}
.site-footer span{margin:0 18px}
</style>
</head>
<body>
<header class="site-header abs">
  <div class="brand abs">CAREPLAN360</div>
  <div class="brand-bar abs"></div>
  <nav class="main-nav abs">
    <a class="active" style="left:218px">MEDICARE SUPPLEMENT</a>
    <a style="left:389px">PART D</a>
    <a style="left:454px">HOW TO DECIDE</a>
    <a style="left:573px">LEARN ONLINE</a>
    <a style="left:683px">WHY CAREPLAN360</a>
    <a style="left:826px">BUY NOW</a>
  </nav>
  <div class="header-divider abs" style="left:898px"></div>
  <div class="contact abs">
    <div class="cta">COMPARE RATES &amp; SAVE</div>
    <div class="phone">(555) 010-2938</div>
  </div>
  <div class="header-divider abs" style="left:1102px"></div>
  <div class="social abs"><span></span><span></span><span></span><span></span></div>
</header>

<section class="hero abs"></section>
<div class="why-card abs" role="img" aria-label="Photo of two business people reviewing a tablet">
  <h2>Why Us</h2>
  <p>Lorem Ipsum is simply dummy has been the industry's text of the printing and typesetting industry.</p>
  <a class="more" href="#">Read More &rarr;</a>
</div>
<div class="video abs">
  <div class="video-frame" role="img" aria-label="Video still of a team meeting around a table">
    <div class="ribbon">CAREPLAN360</div>
    <div class="play">
      <svg width="64" height="64" viewBox="0 0 64 64"><path d="M26 20 L45 32 L26 44 Z" fill="#fff"/></svg>
    </div>
    <div class="controls">
      <svg width="420" height="34" viewBox="0 0 420 34">
        <path d="M16 11 L26 17 L16 23 Z" fill="#fff"/>
        <rect x="40" y="15.5" width="306" height="3" rx="1.5" fill="#ddd"/>
        <rect x="40" y="15.5" width="125" height="3" rx="1.5" fill="#c62a20"/>
        <path d="M362 14 h4 l5 -4 v14 l-5 -4 h-4 Z" fill="#fff"/>
        <path d="M374 13 q3 4 0 8" stroke="#fff" fill="none" stroke-width="1.5"/>
        <rect x="389" y="12" width="15" height="10" fill="none" stroke="#fff" stroke-width="2"/>
      </svg>
    </div>
  </div>
</div>

<section class="action-band abs">
  <a style="left:142px">Compare Rates</a>
  <a style="left:422px">Buy Now</a>
  <div class="focus abs"></div>
  <a style="left:694px">Learn Online</a>
  <a style="left:977px">Get Expert Help</a>
</section>

<div class="card quote-card abs">
  <p>Lorem Ipsum is simply dummy text of the printing and typesetting industry. Lorem Ipsum has been the industry's standard dummy text ever &nbsp;an unknown printer took a galley of type since the 1500s, when an unknown printer took a galley of type and scrambled.</p>
</div>
<div class="card reviews abs">
  <h3>What Peaple are Saying</h3>
  <p>Lorem Ipsum is simply dummy text of the printing and typesetting industry. Lorem Ipsum been the industry standard dummy since the 1500s.</p>
  <div class="by">*****Marla Quentin</div>
</div>
<div class="card updates abs">
  <h3>Monthly Updates</h3>
  <div class="signup"><div class="email">Email Address</div><div class="btn">Sign Up</div></div>
  <div class="note">Enter Email for Customized Monthly Rate Updates &amp; More</div>
</div>

<footer class="site-footer abs">
  <span>Careplan360</span>|<span>Sitemap</span>|<span>Buy Now</span>|<span>Blog</span>|<span>Login</span>
</footer>
</body>
</html>
```